Harborline Cremations Postcard

Postcards to explain our services. Modern yet professional remembering this is about people's loved one's. Use Poppins font and Century Gothic.

Target Market(s)

People who's loved ones are going to pass away.

Font styles to use
Sans Serif

Colors
33a6d7

Requirements
Must have
• Logo, website, all the information from the attachments.

```html
<!DOCTYPE html>
<html lang="en">
<head>
<meta charset="utf-8">
<title>Harborline Cremations Postcard</title>
<link rel="stylesheet" href="https://fonts.googleapis.com/css2?family=Poppins:wght@300;400;500;600;700&display=swap">
<style>
  :root {
    --brand-blue: #33a6d7;
    --deep-blue: #1a8fd0;
    --wave-blue: #2f7fcf;
    --brand-orange: #f47b20;
    --sun-gold: #fbb417;
    --ink-white: #ffffff;
    --stage: #8b8d91;
    --line-grey: #5c5c5c;
  }
  * { box-sizing: border-box; margin: 0; padding: 0; }
  html, body { width: 793px; height: 1200px; overflow: hidden; }
  body {
    background: var(--stage);
    font-family: "Poppins", sans-serif;
    position: relative;
  }
  .postcard {
    position: absolute;
    left: 72px;
    width: 1094px;
    height: 827px;
    transform: scale(0.5922);
    transform-origin: top left;
    background: var(--ink-white);
    overflow: hidden;
  }
  .postcard--front { top: 62px; }
  .postcard--back { top: 618px; }
  .card-art { position: absolute; inset: 0; width: 1094px; height: 827px; }
  .abs { position: absolute; }

  /* Front */
  .headline {
    left: 0; width: 1094px; text-align: center; white-space: nowrap;
    color: var(--ink-white); font-weight: 600; font-size: 80px;
    line-height: 1; letter-spacing: -0.5px;
    text-shadow: 0 3px 6px rgba(120, 50, 0, 0.35);
  }
  .headline--top { top: 64px; }
  .headline--main { top: 146px; }
  .service-line {
    left: 0; width: 1094px; text-align: center; white-space: nowrap;
    color: var(--ink-white); font-weight: 600; font-size: 46px; line-height: 1;
    text-shadow: 0 2px 4px rgba(120, 50, 0, 0.3);
  }
  .service-line--one { top: 286px; }
  .service-line--two { top: 344px; }
  .rule { height: 3px; background: var(--ink-white); top: 376px; width: 146px; }
  .rule--left { left: 123px; }
  .rule--right { left: 806px; }
  .price-badge {
    left: 818px; top: 415px; width: 214px; height: 214px; border-radius: 50%;
    background: var(--deep-blue); border: 5px solid var(--ink-white);
    color: var(--ink-white); text-align: center;
  }
  .price-badge__amount { display: block; margin-top: 42px; font-size: 78px; font-weight: 600; line-height: 1; letter-spacing: -3px; }
  .price-badge__amount sup { font-size: 36px; vertical-align: 30px; letter-spacing: 0; }
  .price-badge__label { display: block; margin-top: 8px; font-size: 23px; font-weight: 500; }
  .brand-mark { left: 120px; top: 590px; width: 180px; height: 180px; border-radius: 50%; background: var(--brand-orange); }
  .brand-name {
    left: 40px; width: 380px; top: 772px; text-align: center; white-space: nowrap;
    color: var(--brand-blue); font-weight: 600; font-size: 30px; line-height: 1;
  }
  .phone-pill {
    display: flex; align-items: center; justify-content: center; gap: 22px;
    white-space: nowrap;
    background: var(--brand-orange); border: 5px solid var(--ink-white); border-radius: 44px;
    box-shadow: 0 6px 10px rgba(0, 0, 0, 0.35);
    color: var(--ink-white); font-weight: 500; line-height: 1;
  }
  .phone-pill--front { left: 460px; top: 671px; width: 568px; height: 86px; font-size: 60px; }
  .phone-pill--back { left: 48px; top: 663px; width: 444px; height: 82px; font-size: 46px; gap: 10px; letter-spacing: -0.5px; }
  .phone-pill svg { flex: none; }
  .web-address {
    left: 440px; width: 604px; top: 779px; text-align: center; white-space: nowrap;
    color: var(--deep-blue); font-weight: 600; font-size: 23px; letter-spacing: -0.3px;
  }

  /* Back */
  .inclusions { left: 52px; top: 52px; list-style: none; color: var(--ink-white); }
  .inclusions li { position: relative; padding-left: 36px; font-size: 27px; font-weight: 500; line-height: 33px; margin-bottom: 8px; white-space: nowrap; }
  .inclusions li svg { position: absolute; left: 0; top: 9px; }
  .inclusions .note { font-weight: 300; display: block; }
  .contact-email {
    left: 44px; top: 758px; display: flex; align-items: center; gap: 14px; white-space: nowrap;
    color: var(--ink-white); font-size: 27px; font-weight: 500;
  }
  .stamp-box { left: 924px; top: 50px; width: 126px; height: 141px; border: 1.5px solid var(--line-grey); }
  .address-line { left: 684px; width: 353px; height: 1.5px; background: var(--line-grey); }
</style>
</head>
<body>

<section class="postcard postcard--front" aria-label="Postcard front">
  <svg class="card-art" viewBox="0 0 1094 827">
    <defs>
      <linearGradient id="sunsetSea" x1="0" y1="0" x2="0" y2="1">
        <stop offset="0" stop-color="#fbb417"/>
        <stop offset="0.4" stop-color="#f7941d"/>
        <stop offset="0.75" stop-color="#ef7d1a"/>
        <stop offset="1" stop-color="#e9902f"/>
      </linearGradient>
    </defs>
    <path role="img" aria-label="Photo of a golden sunset over the ocean and beach" fill="url(#sunsetSea)"
      d="M0 0H1094V548C900 640 620 650 330 560C200 520 90 510 0 528Z"/>
    <path fill="var(--wave-blue)"
      d="M0 528C90 510 200 520 330 560C620 650 900 640 1094 548V590C900 665 620 668 330 585C200 550 90 560 0 590Z"/>
    <path fill="var(--brand-blue)"
      d="M0 528C90 510 200 520 330 560C620 650 900 640 1094 548V566C900 655 620 662 330 575C200 540 90 548 0 570Z"/>
    <path fill="var(--ink-white)"
      d="M0 590C90 560 200 550 330 585C620 668 900 665 1094 590V827H0Z"/>
  </svg>

  <h1 class="abs headline headline--top">ONLINE</h1>
  <h1 class="abs headline headline--main">ARRANGEMENT CENTER</h1>
  <p class="abs service-line service-line--one">Hand Delivery of Cremated Remains</p>
  <span class="abs rule rule--left"></span>
  <p class="abs service-line service-line--two">Miami-Dade County</p>
  <span class="abs rule rule--right"></span>

  <div class="abs price-badge">
    <span class="price-badge__amount"><sup>$</sup>695</span>
    <span class="price-badge__label">All-Inclusive</span>
  </div>

  <span class="abs brand-mark"></span>
  <p class="abs brand-name">Harborline Cremations</p>

  <div class="abs phone-pill phone-pill--front">
    <svg width="52" height="52" viewBox="0 0 24 24" fill="none" stroke="#fff" stroke-width="1.8" stroke-linecap="round" stroke-linejoin="round">
      <path d="M22 16.9v3a2 2 0 0 1-2.2 2 19.8 19.8 0 0 1-8.6-3.1 19.5 19.5 0 0 1-6-6A19.8 19.8 0 0 1 2.1 4.2 2 2 0 0 1 4.1 2h3a2 2 0 0 1 2 1.7c.1.9.4 1.8.7 2.7a2 2 0 0 1-.5 2.1L8 9.8a16 16 0 0 0 6 6l1.3-1.3a2 2 0 0 1 2.1-.4c.9.3 1.8.6 2.7.7a2 2 0 0 1 1.7 2z"/>
      <path d="M15 5a5 5 0 0 1 4 4M15 1a9 9 0 0 1 8 8"/>
    </svg>
    <span>(305) 555-0147</span>
  </div>
  <p class="abs web-address">WWW.HARBORLINECREMATIONSMIAMI.COM</p>
</section>

<section class="postcard postcard--back" aria-label="Postcard back">
  <svg class="card-art" viewBox="0 0 1094 827">
    <defs>
      <linearGradient id="careBlue" x1="0" y1="0" x2="1" y2="1">
        <stop offset="0" stop-color="#2fa0dc"/>
        <stop offset="0.5" stop-color="#5bb6e4"/>
        <stop offset="1" stop-color="#1f93d4"/>
      </linearGradient>
    </defs>
    <path role="img" aria-label="Soft blue-toned photo of comforting held hands"
      fill="url(#careBlue)"
      d="M0 0H498C450 90 445 240 500 370C565 520 600 660 555 827H0Z"/>
    <path fill="var(--brand-orange)"
      d="M568 0H500C440 110 460 260 530 400C600 540 630 680 540 827H600C660 680 640 530 565 400C500 270 500 110 568 0Z"/>
  </svg>

  <ul class="abs inclusions">
    <li><svg width="20" height="16" viewBox="0 0 20 16"><path d="M2 8l6 5L18 2" fill="none" stroke="#fff" stroke-width="4" stroke-linecap="round" stroke-linejoin="round"/></svg>Filing Death Certificate</li>
    <li><svg width="20" height="16" viewBox="0 0 20 16"><path d="M2 8l6 5L18 2" fill="none" stroke="#fff" stroke-width="4" stroke-linecap="round" stroke-linejoin="round"/></svg>Bringing Your Loved<br>One into our Care</li>
    <li><svg width="20" height="16" viewBox="0 0 20 16"><path d="M2 8l6 5L18 2" fill="none" stroke="#fff" stroke-width="4" stroke-linecap="round" stroke-linejoin="round"/></svg>Refrigeration</li>
    <li><svg width="20" height="16" viewBox="0 0 20 16"><path d="M2 8l6 5L18 2" fill="none" stroke="#fff" stroke-width="4" stroke-linecap="round" stroke-linejoin="round"/></svg>Crematory Fee</li>
    <li><svg width="20" height="16" viewBox="0 0 20 16"><path d="M2 8l6 5L18 2" fill="none" stroke="#fff" stroke-width="4" stroke-linecap="round" stroke-linejoin="round"/></svg>Alternative Container<span class="note">(Cardboard)</span></li>
    <li><svg width="20" height="16" viewBox="0 0 20 16"><path d="M2 8l6 5L18 2" fill="none" stroke="#fff" stroke-width="4" stroke-linecap="round" stroke-linejoin="round"/></svg>Temporary Container<span class="note">(Cardboard)</span></li>
    <li><svg width="20" height="16" viewBox="0 0 20 16"><path d="M2 8l6 5L18 2" fill="none" stroke="#fff" stroke-width="4" stroke-linecap="round" stroke-linejoin="round"/></svg>Hand Delivery of Cremated<br>Remains Miami-Dade County</li>
    <li><svg width="20" height="16" viewBox="0 0 20 16"><path d="M2 8l6 5L18 2" fill="none" stroke="#fff" stroke-width="4" stroke-linecap="round" stroke-linejoin="round"/></svg>Medical Examiner Cremation<br>Approval Fee</li>
    <li><svg width="20" height="16" viewBox="0 0 20 16"><path d="M2 8l6 5L18 2" fill="none" stroke="#fff" stroke-width="4" stroke-linecap="round" stroke-linejoin="round"/></svg>1st Copy of Death Certificate</li>
    <li><svg width="20" height="16" viewBox="0 0 20 16"><path d="M2 8l6 5L18 2" fill="none" stroke="#fff" stroke-width="4" stroke-linecap="round" stroke-linejoin="round"/></svg>Online Guestbook</li>
  </ul>

  <div class="abs phone-pill phone-pill--back">
    <svg width="40" height="40" viewBox="0 0 24 24" fill="none" stroke="#fff" stroke-width="1.8" stroke-linecap="round" stroke-linejoin="round">
      <path d="M22 16.9v3a2 2 0 0 1-2.2 2 19.8 19.8 0 0 1-8.6-3.1 19.5 19.5 0 0 1-6-6A19.8 19.8 0 0 1 2.1 4.2 2 2 0 0 1 4.1 2h3a2 2 0 0 1 2 1.7c.1.9.4 1.8.7 2.7a2 2 0 0 1-.5 2.1L8 9.8a16 16 0 0 0 6 6l1.3-1.3a2 2 0 0 1 2.1-.4c.9.3 1.8.6 2.7.7a2 2 0 0 1 1.7 2z"/>
      <path d="M15 5a5 5 0 0 1 4 4M15 1a9 9 0 0 1 8 8"/>
    </svg>
    <span>(305) 555-0147</span>
  </div>

  <p class="abs contact-email">
    <svg width="30" height="24" viewBox="0 0 30 24"><rect x="2" y="3" width="26" height="18" rx="2" fill="none" stroke="#fff" stroke-width="2.5"/><path d="M4 7l11 8 11-8" fill="none" stroke="#fff" stroke-width="2.5"/></svg>
    <span>hello@harborlinecremations.com</span>
  </p>

  <div class="abs stamp-box"></div>
  <div class="abs address-line" style="top:366px"></div>
  <div class="abs address-line" style="top:443px"></div>
  <div class="abs address-line" style="top:521px"></div>
</section>

</body>
</html>
```